Need Packaging Design for Perfume Company

We are Perfume Company looking for concept design we want to design
Shopping bags
Perfume spraying paper
Perfume Box
I need them to look like full set
Our coloring are White, Red and Gold
Pleas find the Attachments file for our logo
We need it to be class and attractive we need it to look simple and class
Reason: Hi,
I want to get more designs because really I didn't like any design

```html
<!DOCTYPE html>
<html lang="en">
<head>
<meta charset="utf-8">
<title>Crescent Bloom Perfume – Packaging Set</title>
<link rel="stylesheet" href="https://fonts.googleapis.com/css2?family=Lora:wght@400;600;700&display=swap">
<style>
  :root {
    --stage: #cfcfcf;
    --red: #e21f26;
    --red-deep: #b7231f;
    --gold: #f2c84b;
    --gold-band: #e9b94a;
    --white: #ffffff;
    --bag-shade: #e7e8e8;
    --handle: #d62027;
    --handle-dark: #8e1a17;
  }
  * { margin: 0; padding: 0; box-sizing: border-box; }
  html, body { width: 1200px; height: 1000px; overflow: hidden; }
  body {
    position: relative;
    background: var(--stage);
    font-family: "Lora", Georgia, serif;
  }

  /* shared wordmark */
  .wordmark { text-align: center; line-height: 1.35; }
  .wordmark .name {
    display: block; font-weight: 700; text-transform: uppercase;
    letter-spacing: 2px;
  }
  .wordmark .sub {
    display: block; font-weight: 400; letter-spacing: 3px;
  }

  /* corner brand lockup */
  .corner-brand {
    position: absolute; top: 130px; right: 52px; width: 160px;
    color: var(--white);
  }
  .corner-brand .mark {
    display: block; width: 34px; height: 34px; margin: 0 auto 14px;
    border: 2px solid var(--white); border-radius: 50%;
  }
  .corner-brand .name { font-size: 13px; }
  .corner-brand .sub { font-size: 12px; }

  /* perfume spraying paper */
  .spray-strip {
    position: absolute; left: 215px; top: 138px;
    width: 1040px; height: 230px;
    transform-origin: 0 0; transform: rotate(30deg);
    background: var(--white); display: flex;
  }
  .spray-strip .strip-head {
    width: 290px; height: 100%; background: var(--red);
    position: relative;
  }
  .spray-strip .strip-head .stripes {
    position: absolute; right: 0; top: 0; height: 100%; width: 74px;
    background: repeating-linear-gradient(90deg,
      var(--white) 0 10px, var(--red) 10px 22px);
    border-left: 1px solid var(--gold);
  }
  .spray-strip .strip-name {
    position: absolute; left: 95px; top: 50%; width: 190px;
    transform: translate(-50%, -50%) rotate(-90deg);
    color: var(--gold);
  }
  .spray-strip .strip-name .name { font-size: 12px; }
  .spray-strip .strip-name .sub { font-size: 11px; }

  /* perfume box */
  .perfume-box {
    position: absolute; left: 120px; top: 445px; width: 330px; height: 515px;
    background: linear-gradient(180deg, var(--red) 0%, var(--red) 60%, var(--red-deep) 100%);
    overflow: hidden;
  }
  .perfume-box .texture {
    position: absolute; inset: 0;
    background: radial-gradient(circle at 50% 40%, rgba(255,255,255,0.10) 0%, rgba(255,255,255,0.04) 45%, rgba(255,255,255,0) 75%);
  }
  .perfume-box .band {
    position: absolute; left: 0; width: 100%; height: 20px;
    background: linear-gradient(180deg,
      var(--gold-band) 0 2px, var(--red-deep) 2px 7px,
      var(--gold-band) 7px 9px, var(--red-deep) 9px 18px, var(--gold-band) 18px 20px);
  }
  .perfume-box .band.top { top: 8px; }
  .perfume-box .band.bottom { bottom: 8px; }
  .perfume-box .box-name {
    position: absolute; left: 0; right: 0; top: 256px; color: var(--gold);
  }
  .perfume-box .box-name .name { font-size: 14px; }
  .perfume-box .box-name .sub { font-size: 14px; }

  /* shopping bag */
  .shopping-bag { position: absolute; left: 595px; top: 140px; width: 412px; height: 825px; }
  .shopping-bag .handles { position: absolute; left: 0; top: 0; width: 412px; height: 230px; }
  .shopping-bag .bag-face {
    position: absolute; left: 0; top: 198px; width: 412px; height: 627px;
    background: linear-gradient(180deg, var(--white) 0%, var(--white) 40%, var(--bag-shade) 83%, var(--white) 83.2%, var(--white) 100%);
    overflow: hidden;
  }
  .shopping-bag .texture {
    position: absolute; inset: 0;
    background: radial-gradient(circle at 50% 40%, rgba(242,182,176,0.22) 0%, rgba(242,182,176,0.08) 50%, rgba(242,182,176,0) 80%);
  }
  .shopping-bag .contact-line {
    position: absolute; left: 0; top: 0; width: 412px; height: 90px;
    font-family: "Lora", Georgia, serif; font-size: 9.5px; fill: var(--red);
  }
  .shopping-bag .bag-name {
    position: absolute; left: 0; right: 0; top: 318px; color: var(--gold);
  }
  .shopping-bag .bag-name .name { font-size: 17px; letter-spacing: 2.5px; }
  .shopping-bag .bag-name .sub { font-size: 16px; letter-spacing: 3.5px; }
</style>
</head>
<body>

  <div class="corner-brand wordmark">
    <span class="mark"></span>
    <span class="name">Crescent Bloom</span>
    <span class="sub">perfume</span>
  </div>

  <div class="spray-strip">
    <div class="strip-head">
      <div class="strip-name wordmark">
        <span class="name">Crescent Bloom</span>
        <span class="sub">perfume</span>
      </div>
      <div class="stripes"></div>
    </div>
  </div>

  <div class="perfume-box">
    <div class="texture" role="img" aria-label="Decorative ripple pattern in soft white lines on red"></div>
    <div class="band top"></div>
    <div class="band bottom"></div>
    <div class="box-name wordmark">
      <span class="name">Crescent Bloom</span>
      <span class="sub">perfume</span>
    </div>
  </div>

  <div class="shopping-bag">
    <svg class="handles" viewBox="0 0 412 230" aria-hidden="true">
      <path d="M82 230 C 70 60, 115 5, 175 5 C 238 5, 268 80, 312 230" fill="none" stroke="var(--handle-dark)" stroke-width="7"/>
      <path d="M90 230 C 82 70, 130 12, 200 12 C 270 12, 310 80, 330 230" fill="none" stroke="var(--handle)" stroke-width="7"/>
    </svg>
    <div class="bag-face">
      <div class="texture" role="img" aria-label="Decorative ripple pattern in soft rose lines on white"></div>
      <svg class="contact-line" viewBox="0 0 412 90">
        <defs><path id="contact-arc" d="M55 78 Q 206 -5 357 78"/></defs>
        <text><textPath href="#contact-arc" startOffset="50%" text-anchor="middle">www.crescentbloom  ●  contact@crescentbloom.com  ●  +359880124576</textPath></text>
      </svg>
      <div class="bag-name wordmark">
        <span class="name">Crescent Bloom</span>
        <span class="sub">perfume</span>
      </div>
    </div>
  </div>

</body>
</html>
```